Construction Company

Design a clutter free business card, it can be double-sided utilizing the logo for BDN Ltd simple with all relevant contact information.

Please also a letterhead design to function for the purposes of invoicing, all mail requirements, with header to be distinctive while the footer ties page together and incorporates all necessary information.

For now, please use generic / dummy text and when a winner is selected, I will disclose the contact information.

Hi Designers! Please read the updated brief which includes the design of a business card and letterhead. Thank you!

```html
<!DOCTYPE html>
<html lang="en">
<head>
<meta charset="UTF-8">
<title>BDN Ltd Business Card</title>
<link href="https://fonts.googleapis.com/css2?family=Oswald:wght@600&family=Work+Sans:wght@400;500&display=swap" rel="stylesheet">
<style>
  :root {
    --page: #2b2b2b;
    --card: #1d1d1d;
    --gold: #c9a227;
    --blue: #1a3fb0;
    --ink: #f2f2f2;
  }
  * { margin: 0; padding: 0; box-sizing: border-box; }
  html, body { width: 1200px; height: 900px; overflow: hidden; }
  body {
    background: var(--page);
    font-family: "Work Sans", sans-serif;
    position: relative;
  }
  .card {
    position: absolute;
    left: 250px;
    width: 700px;
    height: 400px;
    background: var(--card);
    border-bottom: 6px solid var(--gold);
    box-shadow: 0 10px 30px rgba(0,0,0,0.45);
  }
  .card--front { top: 30px; }
  .card--back { top: 470px; }

  .brand {
    position: absolute;
    top: 50%;
    left: 50%;
    transform: translate(-50%, -50%);
    display: flex;
    align-items: center;
    gap: 18px;
  }
  .brand__dot {
    width: 34px; height: 34px;
    border-radius: 50%;
    background: var(--gold);
  }
  .brand__name {
    font-family: "Work Sans", sans-serif;
    font-weight: 500;
    font-size: 76px;
    letter-spacing: 2px;
    color: var(--blue);
  }

  .holder {
    position: absolute;
    right: 380px;
    top: 140px;
    text-align: right;
  }
  .holder__name {
    font-family: "Oswald", sans-serif;
    font-weight: 600;
    font-size: 40px;
    letter-spacing: 2px;
    color: var(--gold);
    line-height: 1.1;
  }
  .holder__role {
    font-size: 19px;
    letter-spacing: 1px;
    color: var(--ink);
    margin-top: 2px;
  }
  .divider {
    position: absolute;
    left: 342px;
    top: 142px;
    width: 2px;
    height: 76px;
    background: var(--gold);
  }
  .contact {
    position: absolute;
    left: 368px;
    top: 140px;
    list-style: none;
  }
  .contact li {
    display: flex;
    align-items: center;
    gap: 10px;
    font-size: 19px;
    letter-spacing: 1px;
    color: var(--ink);
    line-height: 27px;
  }
  .contact svg { width: 14px; height: 14px; flex: none; }
  .address {
    position: absolute;
    left: 120px;
    bottom: 40px;
    font-size: 19px;
    letter-spacing: 1px;
    color: var(--ink);
  }
</style>
</head>
<body>
  <section class="card card--front">
    <div class="brand">
      <span class="brand__dot"></span>
      <span class="brand__name">BDN LTD</span>
    </div>
  </section>

  <section class="card card--back">
    <div class="holder">
      <p class="holder__name">DANIEL HART</p>
      <p class="holder__role">Founder</p>
    </div>
    <span class="divider"></span>
    <ul class="contact">
      <li>
        <svg viewBox="0 0 24 24" aria-hidden="true"><path fill="#c9a227" d="M6.6 10.8a15 15 0 0 0 6.6 6.6l2.2-2.2c.3-.3.7-.4 1-.2 1.1.4 2.3.6 3.6.6.6 0 1 .4 1 1V20c0 .6-.4 1-1 1A17 17 0 0 1 3 4c0-.6.4-1 1-1h3.5c.6 0 1 .4 1 1 0 1.3.2 2.5.6 3.6.1.3 0 .7-.2 1z"/></svg>
        (555) 214-7390
      </li>
      <li>
        <svg viewBox="0 0 24 24" aria-hidden="true"><rect x="2" y="5" width="20" height="14" fill="none" stroke="#c9a227" stroke-width="2"/><path d="M2 5l10 8 10-8" fill="none" stroke="#c9a227" stroke-width="2"/></svg>
        info@BDN Ltd.com
      </li>
      <li>
        <svg viewBox="0 0 24 24" aria-hidden="true"><circle cx="12" cy="12" r="10" fill="none" stroke="#c9a227" stroke-width="2"/><ellipse cx="12" cy="12" rx="4" ry="10" fill="none" stroke="#c9a227" stroke-width="2"/><path d="M2 12h20" stroke="#c9a227" stroke-width="2"/></svg>
        www.BDN Ltd.com
      </li>
    </ul>
    <p class="address">2780 Harbor Lane Riverton, DE 19120</p>
  </section>
</body>
</html>
```